New Company Business Card Design

I have a new company logo and I want a new business card design. I dont know if the logo file i attached is in the correct format or quality. We are a New York City Specialty construction Firm specializing in high risk out of the box projects. I want a simple and classy business card that people will his card is as crisp as the work his company does.

Target Market(s)

Clients in the heavy construction industry in New York City

Industry/Entity Type

Construction Company

Contact Information for Business Card

Simple Classy - DIFFERENT

Font styles to use
Other font styles liked:
• Mach the logo font in some way

Colors

Designer to choose colors to be used in the design.

Requirements
Must have
• Uniqueness
Nice to have
• Nothing particular - Just different and classy - Timeless
Should not have
• Goofy Shit or Gimmicky shit

```html
<!DOCTYPE html>
<html lang="en">
<head>
<meta charset="utf-8">
<title>Harlow Rigging, Inc. – Business Card</title>
<link href="https://fonts.googleapis.com/css2?family=Roboto:wght@400;700&display=swap" rel="stylesheet">
<style>
  :root {
    --stage: #e6e6e6;
    --paper: #ffffff;
    --brand-deep: #0a4f96;
    --brand-bright: #1aa3e0;
    --brand-mid: #0273bd;
    --ink: #222222;
    --rule: #d9d9d9;
    --on-brand: #ffffff;
  }
  * { margin: 0; padding: 0; box-sizing: border-box; }
  html, body { width: 1200px; height: 1000px; overflow: hidden; }
  body {
    background: var(--stage);
    font-family: "Roboto", Arial, sans-serif;
    position: relative;
  }
  .card { position: absolute; width: 714px; height: 407px; overflow: hidden; }
  .card--front { left: 242px; top: 62px; background: var(--paper); }
  .card--back {
    left: 244px; top: 530px;
    background: radial-gradient(ellipse at 50% 50%, var(--brand-bright) 0%, #0a8fd4 45%, var(--brand-mid) 100%);
  }
  .wordmark {
    position: absolute;
    display: flex; align-items: center; gap: 12px;
    font-weight: 700; letter-spacing: 1px; white-space: nowrap;
  }
  .wordmark__mark { width: 22px; height: 22px; flex: none; }
  .card--front .wordmark {
    left: 34px; top: 190px; width: 300px;
    font-size: 30px; line-height: 36px; color: var(--brand-deep);
  }
  .card--front .wordmark__mark { background: var(--brand-deep); }
  .card--back .wordmark {
    left: 0; right: 0; top: 180px; justify-content: center;
    font-size: 48px; color: var(--on-brand);
  }
  .card--back .wordmark__mark { width: 32px; height: 32px; background: var(--on-brand); }
  .divider {
    position: absolute; left: 356px; top: 32px;
    width: 3px; height: 344px; background: var(--rule);
  }
  .holder-name {
    position: absolute; left: 374px; top: 50px;
    font-size: 29px; font-weight: 400; color: var(--brand-deep);
  }
  .contact-list { position: absolute; left: 378px; top: 166px; list-style: none; }
  .contact-list li {
    display: flex; align-items: flex-start;
    font-size: 21px; color: var(--ink); line-height: 28px; height: 37px;
    white-space: nowrap;
  }
  .contact-list li.contact--address { height: auto; line-height: 36px; margin-top: -4px; }
  .contact-icon { width: 19px; height: 19px; margin: 4px 13px 0 0; flex: none; }
  .contact--address .contact-icon { margin-top: 8px; }
  .site-url {
    position: absolute; left: 0; right: 0; bottom: 16px;
    text-align: center; font-size: 21px; color: var(--on-brand);
  }
</style>
</head>
<body>

<section class="card card--front">
  <div class="wordmark"><span class="wordmark__mark"></span><span>HARLOW RIGGING,<br>INC.</span></div>
  <div class="divider"></div>
  <h1 class="holder-name">Marcus T. Bellamy</h1>
  <ul class="contact-list">
    <li>
      <svg class="contact-icon" viewBox="0 0 20 20"><circle cx="10" cy="10" r="10" fill="#0a4f96"/><path d="M5 8.5c0-2 10-2 10 0v1h-2.5v-1h-5v1H5z M6.5 10.5h7l1 4h-9z" fill="#fff"/></svg>
      201-555-0148
    </li>
    <li>
      <svg class="contact-icon" viewBox="0 0 20 20"><circle cx="10" cy="10" r="10" fill="#0a4f96"/><path d="M6.5 5l2 .2.8 2.6-1.3 1a7 7 0 0 0 3.2 3.2l1-1.3 2.6.8.2 2c-5 1-9.5-3.5-8.5-8.5z" fill="#fff"/></svg>
      646-555-0172
    </li>
    <li>
      <svg class="contact-icon" viewBox="0 0 20 20"><circle cx="10" cy="10" r="10" fill="#0a4f96"/><rect x="5" y="6.5" width="10" height="7" rx="1" fill="#fff"/><path d="M5.5 7l4.5 3.5L14.5 7" stroke="#0a4f96" stroke-width="1.2" fill="none"/></svg>
      marcus@harlowrig.com
    </li>
    <li>
      <svg class="contact-icon" viewBox="0 0 20 20"><circle cx="10" cy="10" r="9" fill="none" stroke="#0a4f96" stroke-width="1.6"/><ellipse cx="10" cy="10" rx="4" ry="9" fill="none" stroke="#0a4f96" stroke-width="1.4"/><path d="M1 10h18M2.5 5.5h15M2.5 14.5h15" stroke="#0a4f96" stroke-width="1.4"/></svg>
      www.harlowrig.com
    </li>
    <li class="contact--address">
      <svg class="contact-icon" viewBox="0 0 20 20"><circle cx="10" cy="10" r="10" fill="#0a4f96"/><path d="M10 5l5 4.5h-1.5V15h-7V9.5H5z" fill="#fff"/><rect x="8.8" y="11.5" width="2.4" height="3.5" fill="#0a4f96"/></svg>
      <span>118 Dock Road -<br>Bayonne, New Jersey 07002</span>
    </li>
  </ul>
</section>

<section class="card card--back">
  <div class="wordmark"><span class="wordmark__mark"></span>HARLOW RIGGING, INC.</div>
  <p class="site-url">www.harlowrig.com</p>
</section>

</body>
</html>
```